Ad campaign in the solar industry

We are a young, up-and-coming solar module production company searching for a new print ad campaign. The design needs to express the core values of our company: a smart product, local support and service, as well as environmental awareness.
We would appreciate designs that communicate the advantages of renewable energy with a strong, clear message. Additionally, the concept should include visually appealing graphics to engage audiences throughout Europe and the US. Design concepts should be drafted in English. The design will appear in many forms; it will be adapted for publications, signage and online campaigns.
We value out-of-the box thinking, a modern approach, and creativity that goes beyond the usual solar ad.

```html
<!DOCTYPE html>
<html lang="en">
<head>
<meta charset="utf-8">
<title>Delivering Safe Solar – Brightfield</title>
<link rel="stylesheet" href="https://fonts.googleapis.com/css2?family=PT+Sans:ital,wght@0,400;0,700;1,700&family=Caveat:wght@500&display=swap">
<style>
  :root {
    --panel-blue: #1f5fd0;
    --sky-blue: #8fd3f2;
    --sky-light: #d8f1fb;
    --grass-green: #7ec43a;
    --headline-orange: #f7a21b;
    --bullet-blue: #4fb2ea;
    --card-white: rgba(255, 255, 255, 0.72);
    --map-blue: #c9ecf8;
    --paper: #ffffff;
    --brand-grey: #4a4a4a;
    --tag-green: #8cc63f;
  }
  * { margin: 0; padding: 0; box-sizing: border-box; }
  html, body { width: 1200px; height: 870px; overflow: hidden; background: var(--paper); }
  .ad {
    position: relative;
    width: 1200px;
    height: 870px;
    overflow: hidden;
    font-family: "PT Sans", "Trebuchet MS", sans-serif;
  }
  .ad__scene {
    position: absolute;
    inset: 0;
    background:
      radial-gradient(circle at 88% 8%, #ffffff 0 6%, rgba(255,255,255,0) 22%),
      linear-gradient(160deg, var(--panel-blue) 0%, #4a90e2 28%, var(--sky-blue) 48%, var(--sky-light) 60%, #a8d96a 72%, var(--grass-green) 100%);
  }
  .ad__ground {
    position: absolute;
    left: 0;
    top: 0;
    width: 1200px;
    height: 870px;
  }
  .headline {
    position: absolute;
    color: var(--headline-orange);
    font-weight: 700;
    line-height: 1;
    white-space: nowrap;
  }
  .headline__top { left: 470px; top: 44px; font-size: 100px; }
  .headline__main { left: 584px; top: 148px; font-size: 122px; }
  .benefits {
    position: absolute;
    left: 0;
    top: 279px;
    width: 631px;
    height: 301px;
    background: var(--card-white);
    border-radius: 0 10px 10px 0;
    padding: 20px 20px 0 12px;
    color: var(--bullet-blue);
    list-style: none;
  }
  .benefit { position: relative; padding-left: 30px; margin-bottom: 16px; }
  .benefit::before {
    content: "";
    position: absolute;
    left: 4px;
    top: 21px;
    width: 10px;
    height: 10px;
    border-radius: 50%;
    background: var(--bullet-blue);
  }
  .benefit__title { font-size: 45px; font-weight: 700; line-height: 1.1; white-space: nowrap; }
  .benefit__note {
    font-size: 26px;
    font-style: italic;
    font-weight: 700;
    line-height: 1;
    max-width: 480px;
  }
  .benefit__note--single { max-width: none; white-space: nowrap; }
  .brand {
    position: absolute;
    right: 20px;
    top: 548px;
    display: flex;
    flex-direction: column;
    align-items: flex-end;
    gap: 6px;
  }
  .brand__dot {
    width: 150px;
    height: 150px;
    border-radius: 50%;
    background: var(--headline-orange);
    margin-right: 64px;
  }
  .brand__name { font-size: 40px; font-weight: 400; color: var(--brand-grey); line-height: 1; }
  .tagline {
    position: absolute;
    left: 601px;
    top: 790px;
    font-family: "Caveat", cursive;
    font-weight: 500;
    font-size: 62px;
    color: var(--tag-green);
    letter-spacing: 6px;
    line-height: 1;
    white-space: nowrap;
  }
</style>
</head>
<body>
  <main class="ad">
    <div class="ad__scene" role="img" aria-label="Photo of a blue solar panel under a bright sunny sky beside a green grass field"></div>

    <svg class="ad__ground" viewBox="0 0 1200 870">
      <defs>
        <linearGradient id="globe-fade" x1="0" y1="0" x2="1" y2="0">
          <stop offset="0" stop-color="#c9ecf8"/>
          <stop offset="0.55" stop-color="#e6f6fc"/>
          <stop offset="1" stop-color="#ffffff"/>
        </linearGradient>
      </defs>
      <path d="M0 812 Q 480 560 1200 560 L1200 870 L0 870 Z" fill="url(#globe-fade)" role="img" aria-label="Faint world map across the curved white band"/>
    </svg>

    <h1>
      <span class="headline headline__top">Delivering</span>
      <span class="headline headline__main">Safe Solar</span>
    </h1>

    <ul class="benefits">
      <li class="benefit"><p class="benefit__title">Energy from a safe source</p></li>
      <li class="benefit">
        <p class="benefit__title">A safe investment</p>
        <p class="benefit__note benefit__note--single">purchaising a product that is built to last 20+ years</p>
      </li>
      <li class="benefit">
        <p class="benefit__title">A safe product</p>
        <p class="benefit__note">(no moving parts, limited impact on the environment)</p>
      </li>
    </ul>

    <div class="brand">
      <span class="brand__dot"></span>
      <span class="brand__name">Brightfield</span>
    </div>

    <p class="tagline">Go GREEN Go SOLAR</p>
  </main>
</body>
</html>
```